Business card

We need a business card design for our company based in Auckland , New Zealand called 'Kestrel + Design Ltd'. We provide architectural services. We would like to see designs that use the max. three colours (such as white, black, grey) The final design should communicate financial safety and growth."
Also I will provide our company logo. I would like to the logo to be embeded onto our business card.

Target Market(s)

new residential house, alteration & addition & light commericila design & drafting service

Industry/Entity Type

Architecture

Contact Information for Business Card

Company name: kestrel + design Ltd.
Name: Mark Telford
Job title: architectural designer & Design RQC
email address: mark@kdstudio.co.nz
mobile number: 02 5319 6620
web site: www.kdstudio.co.nz

Requirements
Must have
• My project must have..
• - embeded logo (attached company logo)
• I don't have a bigger version for our company logo, but I have one old one, so you can remove the word from it)
• - insert the attached small PDGQ logo & RQC logo
• - creative, simple and clear business card.
• - Max. three colours
Nice to have
• - Here are the samples I would like to share with you: http://www.velmorindex.com/blog/minimalistic-business-card-designs/
• I would like to have my business card like one of the creation.
Should not have
• TBA

```html
<!DOCTYPE html>
<html lang="en">
<head>
<meta charset="utf-8">
<title>Kestrel + Design Ltd — Business Card</title>
<link rel="stylesheet" href="https://fonts.googleapis.com/css2?family=Roboto+Condensed:wght@300;400&display=swap">
<style>
  :root {
    --bg: #d9d9d9;
    --paper: #ffffff;
    --charcoal: #3e3e3e;
    --ink: #222222;
    --orange: #f7941d;
    --badge-grey: #8a8a8a;
  }
  * { margin: 0; padding: 0; box-sizing: border-box; }
  html, body { width: 1200px; height: 1200px; overflow: hidden; }
  body {
    background: var(--bg);
    font-family: "Roboto Condensed", "Arial Narrow", sans-serif;
    position: relative;
  }
  .card {
    position: absolute;
    left: 240px;
    width: 720px;
    height: 408px;
  }
  .card--front { top: 157px; background: var(--paper); }
  .card--back  { top: 636px; background: var(--charcoal); }

  .brand {
    position: absolute;
    display: flex;
    align-items: center;
    gap: 12px;
    font-weight: 400;
    white-space: nowrap;
  }
  .brand__dot { border-radius: 50%; flex: none; }
  .card--front .brand { right: 42px; top: 92px; color: var(--charcoal); font-size: 24px; }
  .card--front .brand__dot { width: 18px; height: 18px; background: var(--charcoal); }
  .card--back .brand { left: 50%; top: 50%; transform: translate(-50%, -50%); color: var(--orange); font-size: 30px; }
  .card--back .brand__dot { width: 22px; height: 22px; background: var(--orange); }

  .person { position: absolute; left: 30px; top: 194px; }
  .person__name { color: var(--orange); font-weight: 300; font-size: 37px; line-height: 1; }
  .person__title { color: var(--ink); font-weight: 300; font-size: 23px; margin-top: 7px; line-height: 1; }

  .divider {
    position: absolute; left: 30px; top: 281px;
    width: 654px; height: 1px; background: var(--orange);
  }

  .contacts { position: absolute; left: 30px; top: 300px; list-style: none; }
  .contacts li {
    display: flex; align-items: center; height: 28px;
    font-weight: 300; font-size: 23px; color: var(--ink);
  }
  .contacts svg { width: 20px; height: 20px; margin-right: 18px; flex: none; }

  .badge { position: absolute; }
  .badge--certification {
    left: 474px; top: 291px; width: 92px; height: 92px;
    border-radius: 50%; background: var(--ink);
  }
  .badge--member {
    left: 586px; top: 305px; width: 90px; height: 66px;
    background: var(--badge-grey);
  }
</style>
</head>
<body>
  <section class="card card--front">
    <div class="brand"><span class="brand__dot"></span><span>kestrel + design Ltd.</span></div>

    <div class="person">
      <h1 class="person__name">Mark Telford</h1>
      <p class="person__title">architectural designer &amp; Design RQC</p>
    </div>

    <div class="divider"></div>

    <ul class="contacts">
      <li>
        <svg viewBox="0 0 20 20" aria-hidden="true"><rect x="1" y="4" width="18" height="12" fill="var(--orange)"/><path d="M1 4 L10 11 L19 4" fill="none" stroke="#fff" stroke-width="1.4"/></svg>
        mark@kdstudio.co.nz
      </li>
      <li>
        <svg viewBox="0 0 20 20" aria-hidden="true"><rect x="5" y="1" width="10" height="18" rx="2" fill="none" stroke="var(--orange)" stroke-width="1.8"/><circle cx="10" cy="16" r="1" fill="var(--orange)"/></svg>
        02 5319 6620
      </li>
      <li>
        <svg viewBox="0 0 20 20" aria-hidden="true"><g fill="none" stroke="var(--orange)" stroke-width="1.4"><circle cx="10" cy="10" r="8.5"/><ellipse cx="10" cy="10" rx="3.8" ry="8.5"/><path d="M1.5 10 H18.5 M3 5.5 H17 M3 14.5 H17"/></g></svg>
        www.kdstudio.co.nz
      </li>
    </ul>

    <div class="badge badge--certification" role="img" aria-label="Certification badge"></div>
    <div class="badge badge--member" role="img" aria-label="Professional membership badge"></div>
  </section>

  <section class="card card--back">
    <div class="brand"><span class="brand__dot"></span><span>kestrel + design Ltd.</span></div>
  </section>
</body>
</html>
```